Packaging Design Project - new spa massage oils brand

We need a packaging design for the products of a new line of oil for massage to be used at spas or by independent professionals. The brand name is "lumina", it's reminiscent of that ethereal moment where you lose track of the day-to-day and focus on yourself while being taken care off with aromatherapy, relaxing music and massage.
The packaging is a 250 ml transparent plastic bottle, the design will be in two labels, a front label with the brand and main design elements (product, net content, brand name) and a back label with more generic info. Both labels are of the same size 4.5 x 9 cm. A picture of the bottle will be provided in a separate file along with some ideas.
We are a start-up company in latin america, therefore the texts should be in spanish. There will be initially four SKU's, however, since we don't have a budget for all, we'll use the winning design and I'll use that as a base to create the other labels.
the four initial SKUs are:
-Rosemary (green pallet of colors)
-Lavender (purple pallet)
-Citrus (orange, yellow)
-Baby (pastels, predominantly blue)
We would expect you to focus on either the rosemary or lavender SKU's since those are our most important ones.
We don't have a logo yet for two reasons 1) budget constraints, 2) less restrictions for you to create the packaging artwork. If it's possible to add a mock-up of a logo it would be great.

the text for the back label (spanish) is:
Una combinación natural de aceites de semillas, flores y plantas para un masaje corporal relajante.
PRECAUCIONES: Mantener fuera del alcance de los niños. Evite el contacto con los ojos.
Este producto es biodegradable. No daña la capa de ozono.

translation (not to be on the lable, only for reference).
a combination of natural oils of seeds, flowers and plants for a relaxing body massage.
WARNING: keep out of reach of children, avoid eye contact.
this product is biodegradable. it doesn't damage the ozone layer.

Front label (spanish):
- lumina (this is the brand name)
- Aceite para masaje corporal con extracto de romero (this is the product description oil for body massage with rosemary extract)
- Frescura y vitalidad (this means freshness and vitality which are the characteristics of the rosemary oil)
- 250 ml (this is the net content)

Target Market(s)

consider that this product is used by professionals, however, the end consumers are mostly women (but not exclusive) of 30-45 years old.

Industry/Entity Type

Baby

Requirements
Nice to have
• -If the proposal could have a logo (even a simple one) it would be very much appreciated.
-Might want to try getting inspiration from other "ethereal" things such as smoke, watter ripples, air, fire, etc.
-A distinctive element of what the product has (for instance a picture or a sketch of a rosemary twig or a lavender flower).
-Colors are very important for these type of products, the whole pallet should be consistent. Consider that the rosemary oil is dark green, lavender is clear.
Should not have
• -Aggressive or excessively bright colors (this is a relaxation product).
-If you consider using a smoke texture, it should avoid dark, black shades that smoke usually evanesces into.
-Too polluted labels.

```html
<!DOCTYPE html>
<html lang="es">
<head>
<meta charset="utf-8">
<title>lumina Citrus — etiquetas</title>
<link href="https://fonts.googleapis.com/css2?family=PT+Sans+Narrow:wght@400;700&family=Parisienne&family=Quicksand:wght@600&display=swap" rel="stylesheet">
<style>
  :root {
    --canvas: #ffffff;
    --label-yellow: #fbd23c;
    --band-yellow: #fbd02f;
    --deep-orange: #f6a11c;
    --text-orange: #ef8a2e;
    --script-gold: #f2b128;
    --rule-orange: #ef8f45;
    --white: #ffffff;
  }
  * { box-sizing: border-box; margin: 0; padding: 0; }
  html, body { width: 979px; height: 1200px; overflow: hidden; background: var(--canvas); }
  .canvas { position: relative; width: 979px; height: 1200px; }

  .label {
    position: absolute; top: 400px; width: 260px; height: 600px; overflow: hidden;
    font-family: "PT Sans Narrow", sans-serif; color: var(--text-orange); text-align: center;
  }
  .label--front { left: 130px; background: var(--white); }
  .label--back { left: 565px; background: var(--label-yellow); }

  .brand {
    position: absolute; left: 0; right: 0;
    font-family: "Quicksand", sans-serif; font-weight: 600; font-size: 48px;
    color: var(--white); letter-spacing: 0.5px; line-height: 1;
  }
  .brand-dot {
    display: inline-block; width: 12px; height: 12px; border-radius: 50%;
    background: var(--white); margin-left: 6px; vertical-align: middle;
  }
  .label--front .brand { top: 58px; text-align: left; padding-left: 24px; }
  .label--back .brand { top: 50px; }

  .smoke-art {
    position: absolute; left: 0; top: 0; width: 100%; height: 300px;
    background: linear-gradient(180deg, var(--deep-orange) 0%, #f8b932 18%, #fbe07a 45%, #fdf1c4 72%, var(--white) 100%);
  }

  .variant {
    position: absolute; left: 0; right: 0;
    font-family: "Parisienne", cursive; font-size: 36px; color: var(--script-gold); line-height: 1;
  }
  .label--front .variant { top: 284px; }
  .label--back .variant { top: 108px; color: var(--rule-orange); }

  .divider-mark {
    position: absolute; left: 50%; width: 10px; height: 6px; margin-left: -5px;
    border-radius: 3px; background: var(--script-gold);
  }
  .label--back .divider-mark { background: var(--white); }

  .text { position: absolute; left: 0; right: 0; }
  .description { top: 341px; font-weight: 700; font-size: 18px; line-height: 24px; }
  .tagline { top: 436px; font-size: 17px; }
  .net-content { top: 510px; font-size: 17px; }

  .band { position: absolute; left: 0; bottom: 0; width: 100%; height: 48px; }

  .rule { position: absolute; left: 0; width: 100%; height: 1.5px; background: var(--rule-orange); }
  .rule--top { top: 12px; }
  .rule--bottom { top: 594px; }

  .intro { top: 176px; font-weight: 700; font-size: 17.5px; line-height: 22px; }
  .precautions { top: 326px; font-size: 16.5px; line-height: 22px; }
  .eco { top: 447px; font-size: 16.5px; line-height: 22px; }
</style>
</head>
<body>
<main class="canvas">

  <section class="label label--front" aria-label="Etiqueta frontal">
    <div class="smoke-art" role="img" aria-label="Humo translúcido en tonos naranja y amarillo que se desvanece en blanco"></div>
    <div class="brand">lumina<span class="brand-dot"></span></div>
    <div class="variant">Citrus</div>
    <p class="text description">Aceite para masaje corporal<br>con extracto de romero</p>
    <span class="divider-mark" style="top:412px" role="img" aria-label="Separador"></span>
    <p class="text tagline">Frescura y vitalidad</p>
    <span class="divider-mark" style="top:485px" role="img" aria-label="Separador"></span>
    <p class="text net-content">250 ml</p>
    <svg class="band" viewBox="0 0 260 48" preserveAspectRatio="none" aria-hidden="true">
      <path d="M0 4 Q130 -4 260 4 L260 48 L0 48 Z" fill="var(--band-yellow)"/>
      <path d="M0 40 Q130 30 260 40" fill="none" stroke="var(--white)" stroke-width="2"/>
    </svg>
  </section>

  <section class="label label--back" aria-label="Etiqueta posterior">
    <span class="rule rule--top"></span>
    <div class="brand">lumina<span class="brand-dot"></span></div>
    <div class="variant">Citrus</div>
    <p class="text intro">Una combinación natural<br>de aceites de semillas,<br>flores y plantas para<br>un masaje corporal relajante.</p>
    <span class="divider-mark" style="top:293px" role="img" aria-label="Separador"></span>
    <p class="text precautions">PRECAUCIONES:<br>Mantener fuera del<br>alcance de los niños.<br>Evite el contacto con los ojos.</p>
    <p class="text eco">Este producto es biodegradable.<br>No daña la capa de ozono.</p>
    <span class="divider-mark" style="top:531px" role="img" aria-label="Separador"></span>
    <span class="rule rule--bottom"></span>
  </section>

</main>
</body>
</html>
```